Silicone product manufacturer needs name card

we are a silicone proudct manufacturer, need a name card.
Updates

Dear All, Pls use the following information for the name card. Maris Odell Marketing Manager Mobile : HK (852) 64839205 : CN (86) 13957204416 Tel : 852-24776150 Fax : 852-28364471 Rm705,7/F, Lok Tin Ind. Ctr., 24-26 Pak Fung St., Kwun Tong, HK China Office : Tel:86-796-85302617 Fax : 86-769-83651274 5-6/F, Rui Kang Building, No. 47 BeiLin Road, Shi Pai Wan Town, Dong Guan City, PRC China Factory Norvik Technology Ltd Tai Lun Technology Ltd Mei Sun Fat (F.S) Silicone Products Co. Ltd Pelvane Technology Ltd Slogan on the name card : We are your best Business Partner With ISO9001 / ISO14001 / TS16949 LOGO Any query, pls contact me at marisodell@qorvent-mail.net Thanks, maris

Reason: Dear All, Still can't choose the right one. Thanks, Maris

Reason: still not confirm

Reason: working on revision. thanks

Reason: revising the design with designer. thanks

Reason: revising with designer ! thanks

Industry/Entity Type

Manufacturer

```html
<!DOCTYPE html>
<html lang="en">
<head>
<meta charset="UTF-8">
<title>Maris Odell – Name Card</title>
<link href="https://fonts.googleapis.com/css2?family=Arimo:ital,wght@0,400;0,700;1,400&display=swap" rel="stylesheet">
<style>
  :root {
    --card-bg: #ffffff;
    --ink: #000000;
    --stroke-grey: #cfcfcf;
    --stroke-yellow: #f6ecb0;
    --stroke-blue: #cde6f0;
    --stroke-red: #f3c9c9;
    --stroke-green: #e3ecc4;
  }
  html, body {
    margin: 0;
    padding: 0;
    overflow: hidden;
    background: var(--card-bg);
  }
  .card {
    position: relative;
    width: 1200px;
    height: 700px;
    background: var(--card-bg);
    overflow: hidden;
    font-family: "Arimo", Arial, sans-serif;
    color: var(--ink);
  }
  .brush-backdrop {
    position: absolute;
    left: 290px;
    top: 50px;
    width: 580px;
    height: 590px;
  }
  .name, .title, .slogan {
    position: absolute;
    left: 0;
    width: 1168px;
    margin: 0;
    text-align: center;
    white-space: nowrap;
  }
  .name {
    top: 160px;
    font-size: 156px;
    font-weight: 700;
    line-height: 1;
    letter-spacing: -1px;
  }
  .title {
    top: 318px;
    font-size: 62px;
    font-weight: 400;
    line-height: 1;
  }
  .mobile {
    position: absolute;
    top: 474px;
    left: 128px;
    margin: 0;
    font-size: 35px;
    line-height: 1;
    white-space: nowrap;
  }
  .mobile .cn {
    position: absolute;
    left: 550px;
    top: 0;
  }
  .slogan {
    top: 556px;
    font-size: 72px;
    font-style: italic;
    line-height: 1;
  }
</style>
</head>
<body>
  <div class="card">
    <svg class="brush-backdrop" viewBox="0 0 580 590" role="img" aria-label="Faint diagonal colourful brush strokes decoration">
      <defs>
        <linearGradient id="brushTone" x1="0" y1="1" x2="1" y2="0">
          <stop offset="0" stop-color="var(--stroke-red)"/>
          <stop offset="0.35" stop-color="var(--stroke-grey)"/>
          <stop offset="0.6" stop-color="var(--stroke-blue)"/>
          <stop offset="0.8" stop-color="var(--stroke-yellow)"/>
          <stop offset="1" stop-color="var(--stroke-green)"/>
        </linearGradient>
        <radialGradient id="brushFade" cx="0.5" cy="0.5" r="0.5">
          <stop offset="0" stop-color="#fff" stop-opacity="1"/>
          <stop offset="1" stop-color="#fff" stop-opacity="0"/>
        </radialGradient>
        <mask id="brushMask">
          <rect width="580" height="590" fill="url(#brushFade)"/>
        </mask>
      </defs>
      <ellipse cx="290" cy="295" rx="300" ry="200" transform="rotate(-40 290 295)"
               fill="url(#brushTone)" opacity="0.75" mask="url(#brushMask)"/>
    </svg>

    <h1 class="name">Maris Odell</h1>
    <p class="title">Marketing Manager</p>
    <p class="mobile">
      <span class="hk">Mobile : HK (852) 64839205</span>
      <span class="cn">CN (86) 13957204416</span>
    </p>
    <p class="slogan">“We are your best”</p>
  </div>
</body>
</html>
```